Sign Design

We already have a logo, but would like to design 2 x signs.
Sign 1:
Dimensions 1500mm wide x 2500m high.
Information to include on sign: - Clinic name and logo (attached)
- the word "DENTIST "
- Street number (which is 348)
Phone number (which is 6153 4097)

Sign 2:
Dimensions: 800mm wide x 600mm high

```html
<!DOCTYPE html>
<html lang="en">
<head>
<meta charset="utf-8">
<title>Larkmoor Dental Care – Sign Designs</title>
<link rel="stylesheet" href="https://fonts.googleapis.com/css2?family=Arimo:wght@400&family=Questrial&display=swap">
<style>
  :root {
    --page: #ffffff;
    --forest: #207845;
    --leaf: #4caa46;
    --lime: #a3cc5a;
    --white: #ffffff;
    --caption: #222222;
  }
  * { margin: 0; padding: 0; box-sizing: border-box; }
  html, body { width: 1200px; height: 1015px; overflow: hidden; background: var(--page); }
  .artboard { position: relative; width: 1200px; height: 1015px; }

  .sign { position: absolute; background: var(--forest); overflow: hidden; }
  .sign--tall { left: 55px; top: 84px; width: 474px; height: 788px; }
  .sign--wide { left: 670px; top: 325px; width: 473px; height: 355px; }

  .contact-band {
    position: absolute; left: 0; right: 0; bottom: 0; height: 158px;
    background: var(--leaf);
  }

  .brand-mark { position: absolute; border-radius: 50%; background: var(--lime); }
  .sign--tall .brand-mark { left: 169px; top: 76px; width: 140px; height: 140px; }
  .sign--wide .brand-mark { left: 48px; top: 120px; width: 112px; height: 112px; }

  .brand-name {
    position: absolute;
    font-family: "Arimo", Arial, sans-serif;
    font-weight: 400;
    color: var(--white);
    letter-spacing: -0.03em;
    line-height: 1;
    text-align: right;
  }
  .brand-name__line { display: block; }
  .sign--tall .brand-name { left: 20px; width: 434px; top: 238px; }
  .sign--tall .brand-name__main { font-size: 80px; text-align: center; }
  .sign--tall .brand-name__sub { font-size: 44px; margin-top: 4px; padding-right: 42px; }
  .sign--wide .brand-name { left: 174px; width: 270px; top: 128px; }
  .sign--wide .brand-name__main { font-size: 54px; text-align: left; }
  .sign--wide .brand-name__sub { font-size: 30px; margin-top: 2px; padding-right: 22px; }

  .service {
    position: absolute; left: 0; width: 100%; top: 424px;
    font-family: "Arimo", Arial, sans-serif;
    font-size: 82px; letter-spacing: 0.07em; text-indent: 0.07em;
    color: var(--white); text-align: center; line-height: 1;
  }

  .contact {
    position: absolute; left: 0; width: 100%; top: 654px;
    font-family: "Arimo", Arial, sans-serif;
    font-size: 41px; color: var(--white); text-align: center; line-height: 53px;
  }

  .caption {
    position: absolute;
    font-family: "Questrial", "Century Gothic", sans-serif;
    font-size: 23px; color: var(--caption); white-space: nowrap;
  }
  .caption--tall { left: 74px; top: 903px; }
  .caption--wide { left: 690px; top: 272px; }
</style>
</head>
<body>
<main class="artboard">

  <section class="sign sign--tall" aria-label="Street sign, 1500 by 2500 mm">
    <span class="contact-band" aria-hidden="true"></span>
    <span class="brand-mark" aria-hidden="true"></span>
    <h1 class="brand-name">
      <span class="brand-name__line brand-name__main">Larkmoor</span>
      <span class="brand-name__line brand-name__sub">Dental Care</span>
    </h1>
    <p class="service">DENTIST</p>
    <p class="contact">Street No.348<br>Phone 6153 4097</p>
  </section>
  <p class="caption caption--tall">Dimensions 1500mm wide x 2500m high</p>

  <p class="caption caption--wide">Dimensions: 800mm wide x 600mm high</p>
  <section class="sign sign--wide" aria-label="Wall sign, 800 by 600 mm">
    <span class="brand-mark" aria-hidden="true"></span>
    <h2 class="brand-name">
      <span class="brand-name__line brand-name__main">Larkmoor</span>
      <span class="brand-name__line brand-name__sub">Dental Care</span>
    </h2>
  </section>

</main>
</body>
</html>
```